Label Redesign For Hemp Oil Tincture Bottle*

I need a label redesigned for Marbleleaf Hemp, current bottle label and logo is attached. The current label doesn't standout, not sure if its the font size or colors on the existing label. It is very important to have on the label that this is a Premium Full Spectrum Hemp Oil that is 2000mg. Then after the label is redesigned and approved, I would need to packaging to be designed to match the approved label design.
This Hemp oil has a relaxing effect to help ease mental and emotional stress, tension and worry. The Omega Fatty Acids it contains also naturally improves your mood and overall brain function, causing you to feel more alert and focused. Hemp Oil helps with insomnia. Take some 2-3 hours before bedtime, you will feel relaxed yet aware of how tired you are that it will lead to a good night's sleep. Hemp Oil helps ease chronic pain and inflammation from conditions such as arthritis, fibromyalgia, lupus, and MS. As a pain relief supplement, it is a safer, natural, non-chemical and non-addictive alternative to prescription painkillers.

Target Market(s)

Adults

Industry/Entity Type

Supplement

Font styles to use
Serif
Sans Serif

Colors

Designer to choose colors to be used in the design.

Requirements
Must have
• All information thats on current label but where it says 750 in the front of the existing label, it needs to say 2000. The 2000 should be prominent on the label.

```html
<!DOCTYPE html>
<html lang="en">
<head>
<meta charset="utf-8">
<title>Marbleleaf Hemp Label</title>
<link href="https://fonts.googleapis.com/css2?family=Playfair+Display:wght@400&family=Montserrat:wght@400;700;800&family=Mrs+Saint+Delafield&display=swap" rel="stylesheet">
<style>
  :root {
    --backdrop: #e4fbea;
    --label: #ffffff;
    --teal: #3f7a74;
    --teal-deep: #375d5a;
    --ink-grey: #555555;
    --mark-green: #9cc46a;
  }
  html, body {
    margin: 0;
    padding: 0;
    width: 1002px;
    height: 1200px;
    overflow: hidden;
    background: var(--backdrop);
  }
  .label {
    position: absolute;
    left: 61px;
    top: 129px;
    width: 880px;
    height: 941px;
    background: var(--label);
    overflow: hidden;
  }
  .brand {
    position: absolute;
    left: 0;
    width: 100%;
    top: 60px;
    text-align: center;
  }
  .brand-dot {
    width: 96px;
    height: 96px;
    border-radius: 50%;
    background: var(--mark-green);
    margin: 0 auto;
  }
  .brand-name {
    margin-top: 12px;
    font-family: "Playfair Display", serif;
    font-size: 45px;
    letter-spacing: 2px;
    color: var(--ink-grey);
    line-height: 1;
  }
  .product-name {
    position: absolute;
    left: 94px;
    top: 262px;
    margin: 0;
    font-family: "Playfair Display", serif;
    font-weight: 400;
    font-size: 73px;
    letter-spacing: 2px;
    color: var(--teal);
    line-height: 1;
  }
  .spectrum-pill {
    position: absolute;
    left: 96px;
    top: 405px;
    width: 465px;
    height: 43px;
    border-radius: 22px;
    background: var(--teal-deep);
    color: #fff;
    font-family: "Montserrat", sans-serif;
    font-weight: 700;
    font-size: 26px;
    letter-spacing: 2.5px;
    line-height: 43px;
    text-align: center;
  }
  .strength {
    position: absolute;
    left: 96px;
    top: 478px;
    display: flex;
    align-items: baseline;
    gap: 16px;
  }
  .strength-number {
    font-family: "Montserrat", sans-serif;
    font-weight: 800;
    font-size: 52px;
    letter-spacing: 2px;
    color: var(--teal-deep);
  }
  .strength-unit {
    font-family: "Mrs Saint Delafield", cursive;
    font-size: 58px;
    color: var(--teal-deep);
  }
  .flavor {
    position: absolute;
    left: 94px;
    top: 540px;
    font-family: "Montserrat", sans-serif;
    font-weight: 400;
    font-size: 42px;
    letter-spacing: 1px;
    color: var(--teal);
  }
  .benefits-band {
    position: absolute;
    left: 0;
    top: 619px;
    width: 563px;
    height: 235px;
    background: var(--teal-deep);
    border-radius: 0 82px 82px 0;
  }
  .benefits {
    list-style: none;
    margin: 0;
    padding: 0;
    position: absolute;
    left: 150px;
    top: 42px;
  }
  .benefits li {
    font-family: "Playfair Display", serif;
    font-size: 27px;
    letter-spacing: 2.5px;
    color: #fff;
    line-height: 38.5px;
    position: relative;
    padding-left: 30px;
  }
  .benefits li::before {
    content: "";
    position: absolute;
    left: 0;
    top: 15px;
    width: 11px;
    height: 11px;
    border-radius: 50%;
    background: #fff;
  }
  .volume-badge {
    position: absolute;
    left: 620px;
    top: 651px;
    width: 180px;
    text-align: center;
  }
  .volume-text {
    margin-top: 22px;
    font-family: "Playfair Display", serif;
    font-size: 15px;
    letter-spacing: 1px;
    line-height: 19px;
    color: var(--ink-grey);
  }
</style>
</head>
<body>
  <main class="label">
    <div class="brand">
      <div class="brand-dot"></div>
      <div class="brand-name">Quietroot</div>
    </div>

    <h1 class="product-name">Marbleleaf Hemp</h1>
    <div class="spectrum-pill">PREMIUM FULL SPECTRUM</div>

    <div class="strength">
      <span class="strength-number">2000</span>
      <span class="strength-unit">hemp oil</span>
    </div>
    <div class="flavor">Natural Peppermint Flavor</div>

    <div class="benefits-band">
      <ul class="benefits">
        <li>STRESS RELIEF</li>
        <li>ANTI-INFLAMMATORY</li>
        <li>GET BETTER SLEEP</li>
        <li>PURE &amp; ORGANIC</li>
      </ul>
    </div>

    <div class="volume-badge">
      <svg width="90" height="102" viewBox="0 0 90 102" aria-hidden="true">
        <path d="M22 0 C30 14 38 24 38 34 A16 16 0 0 1 6 34 C6 24 14 14 22 0 Z" fill="#375d5a"/>
        <path d="M52 18 C64 38 80 54 80 72 A28 28 0 0 1 24 72 C24 54 40 38 52 18 Z" fill="#375d5a" stroke="#ffffff" stroke-width="4"/>
      </svg>
      <div class="volume-text">1FLOZ (30ML)<br>DIETARY<br>SUPPLEMENT</div>
    </div>
  </main>
</body>
</html>
```